Organic skincare label - minimalist, earthy, luxe design needed!

I need a label design for a luxury natural skin care line called "Velka Botanix". Velka means 'earth' in Swahili. I would like the design to embody an earthy feel but be minimalistic and give a luxe vibe. My first product will be a Tumeric and Neem Scrub.

The size of the jar is 8oz, label dimensions should be (1.625" Tall x 8.5" Wide)
I will be making other products too such as; oils + toners so I feel free to do labels for glass bottles and/or spray bottles as well.

Forest green, light pinks/nudes/beige, grey, white, gold, are colors that can be used (not all have to be used).

I have included pictures of some things I've worked on myself as well as my original logo design but I need to simplify the logo, no circle around it.
Feel free to get creative.

Thank you! :)
Updates

Target Market(s)

Socially Conscious, Beauty Enthusiast, Minimalist

Industry/Entity Type

Skin Care

Font styles to use
Sans Serif
Other font styles liked:
• "Wonderlove doodle" is the font used for "Velka" in the logo. Feel free to use that or change it as you see fit.

Requirements
Must have
• Simplistic design
would like to stick to a font close to the ones in the logo. Either the one used for the name "Velka" OR the one that the slogan "Rooted Rituals" uses.

I have also included some pictures to capture the aesthetic of my social media and website.

Gender neutral

```html
<!DOCTYPE html>
<html lang="en">
<head>
<meta charset="utf-8">
<title>Velka Botanix – Tumeric &amp; Neem Scrub Label</title>
<link rel="stylesheet" href="https://fonts.googleapis.com/css2?family=Lato:wght@400;700&display=swap">
<style>
  :root {
    --canvas-bg: #f1efed;
    --label-nude: #dca892;
    --label-ink: #ffffff;
    --rule: rgba(255, 255, 255, 0.85);
  }
  html, body {
    margin: 0;
    padding: 0;
    width: 1200px;
    height: 1200px;
    overflow: hidden;
    background: var(--canvas-bg);
  }
  .canvas {
    width: 1200px;
    height: 1200px;
    display: flex;
    align-items: center;
    justify-content: center;
  }
  .label {
    width: 1140px;
    height: 236px;
    background: var(--label-nude);
    color: var(--label-ink);
    font-family: "Lato", sans-serif;
    display: flex;
    flex-direction: column;
    align-items: center;
    justify-content: center;
    text-align: center;
    box-sizing: border-box;
    padding-top: 4px;
  }
  .brand-name {
    margin: 0;
    font-weight: 400;
    font-size: 15px;
    letter-spacing: 2.2px;
    text-transform: uppercase;
  }
  .brand-tagline {
    margin: 7px 0 0;
    font-weight: 400;
    font-size: 8px;
    letter-spacing: 1.4px;
    text-transform: uppercase;
  }
  .product-name {
    margin: 24px 0 0;
    font-weight: 700;
    font-size: 18px;
    letter-spacing: 2.5px;
    text-transform: uppercase;
  }
  .product-rule {
    width: 214px;
    height: 1px;
    background: var(--rule);
    margin: 9px 0 0;
    border: 0;
  }
  .product-description {
    margin: 8px 0 0;
    font-weight: 700;
    font-size: 10px;
    line-height: 17px;
    letter-spacing: 0.4px;
  }
  .product-size {
    margin: 14px 0 0;
    font-weight: 400;
    font-size: 16px;
    letter-spacing: 0.6px;
  }
</style>
</head>
<body>
  <main class="canvas">
    <section class="label" aria-label="Tumeric and Neem Scrub jar label">
      <h1 class="brand-name">Velka Botanix</h1>
      <p class="brand-tagline">Rooted Rituals</p>
      <h2 class="product-name">Tumeric &amp; Neem Scrub</h2>
      <hr class="product-rule">
      <p class="product-description">Lorem ipsum dolor sit amet, consectetur<br>adipiscing elit.</p>
      <p class="product-size">2 oz.</p>
    </section>
  </main>
</body>
</html>
```